Business Card for Consulting Company

I would need a business card for my consulting company - the company brand and logos are defined and shared as part of this project. The proposed design for the business card can be reused as inspiration for my email signature.

```html
<!DOCTYPE html>
<html lang="en">
<head>
<meta charset="utf-8">
<title>Veltamo – Business Card</title>
<link rel="stylesheet" href="https://fonts.googleapis.com/css2?family=Quicksand:wght@500;700&display=swap">
<style>
  :root {
    --backdrop: #1c1c1d;
    --card-dark: #3b3b3d;
    --card-light: #f6f6f6;
    --teal: #13b3b4;
    --ink: #3a3a3c;
    --silver: #d9d9d9;
    --white: #ffffff;
  }
  * { margin: 0; padding: 0; box-sizing: border-box; }
  html, body {
    width: 1200px;
    height: 874px;
    overflow: hidden;
    background: var(--backdrop);
    font-family: "Quicksand", sans-serif;
  }
  .canvas {
    width: 1200px;
    height: 874px;
    display: flex;
    flex-direction: column;
    align-items: center;
    justify-content: center;
    gap: 44px;
  }
  .card {
    position: relative;
    width: 600px;
    height: 343px;
    overflow: hidden;
    box-shadow: 0 18px 40px rgba(0, 0, 0, 0.45);
  }
  .card--front {
    background: var(--card-dark);
    display: flex;
    align-items: center;
    justify-content: center;
  }
  .card--back { background: var(--card-light); }

  .brand {
    display: flex;
    align-items: center;
    gap: 14px;
  }
  .brand__dot {
    width: 22px;
    height: 22px;
    border-radius: 50%;
  }
  .brand__name {
    font-weight: 700;
    font-size: 54px;
    letter-spacing: 1px;
    line-height: 1;
  }
  .card--front .brand__dot { background: var(--silver); }
  .card--front .brand__name { color: var(--silver); }

  .card--back .brand {
    position: absolute;
    left: 0;
    right: 0;
    top: 86px;
    justify-content: center;
  }
  .card--back .brand__dot { background: var(--ink); }
  .card--back .brand__name { color: var(--teal); }

  .band {
    position: absolute;
    left: 0;
    top: 0;
    width: 600px;
    height: 343px;
  }

  .contact {
    position: absolute;
    left: 26px;
    top: 246px;
    list-style: none;
    color: var(--white);
    font-weight: 500;
    font-size: 15px;
    line-height: 1.3;
  }
  .contact__item {
    display: flex;
    align-items: center;
    gap: 10px;
  }
  .contact__icon {
    width: 12px;
    height: 12px;
    flex: none;
  }

  .person {
    position: absolute;
    right: 30px;
    top: 270px;
    text-align: right;
    color: var(--white);
  }
  .person__name {
    font-weight: 700;
    font-size: 21px;
    line-height: 1.15;
  }
  .person__role {
    font-weight: 500;
    font-size: 15px;
    line-height: 1.3;
  }
</style>
</head>
<body>
<main class="canvas">
  <section class="card card--front" aria-label="Card front">
    <div class="brand">
      <span class="brand__dot"></span>
      <span class="brand__name">Veltamo</span>
    </div>
  </section>

  <section class="card card--back" aria-label="Card back">
    <div class="brand">
      <span class="brand__dot"></span>
      <span class="brand__name">Veltamo</span>
    </div>

    <svg class="band" viewBox="0 0 600 343" aria-hidden="true">
      <path d="M0,214 H448 L470,236 L506,222 H600 V343 H0 Z" fill="var(--teal)"/>
      <path d="M0,208 H450 L470,228 L504,215 H600" fill="none" stroke="var(--ink)" stroke-width="3"/>
    </svg>

    <ul class="contact">
      <li class="contact__item">
        <svg class="contact__icon" viewBox="0 0 12 12"><path d="M2.5 0.8 L4.4 3.2 L3.3 4.6 Q4.6 7.2 7.3 8.6 L8.7 7.5 L11.2 9.4 L10 11.2 Q4.5 11 0.9 2.1 Z" fill="var(--white)"/></svg>
        <span>+41 79 000 12 34</span>
      </li>
      <li class="contact__item">
        <svg class="contact__icon" viewBox="0 0 12 12"><rect x="0.5" y="2" width="11" height="8" fill="var(--white)"/><path d="M0.5 2 L6 6.5 L11.5 2" fill="none" stroke="var(--teal)" stroke-width="1.2"/></svg>
        <span>mara.l@veltamo.ch</span>
      </li>
      <li class="contact__item">
        <svg class="contact__icon" viewBox="0 0 12 12"><circle cx="6" cy="6" r="5.5" fill="var(--white)"/><path d="M3 3.5 Q5 4.5 4.5 6.5 Q3 7.5 3.5 9.5 M7.5 2 Q7 4 9 5 Q10.5 6.5 9 9" fill="none" stroke="var(--teal)" stroke-width="1.1"/></svg>
        <span>www.veltamo.ch</span>
      </li>
    </ul>

    <div class="person">
      <p class="person__name">Mara Lindqvist</p>
      <p class="person__role">Founder &amp; CEO</p>
    </div>
  </section>
</main>
</body>
</html>
```